Business Card - Professional Minimalist - Double sided

We appreciate minimalist logo/web/collateral designs that allow design to tell a story. We want to relay a professional image/approach but throwing in a splash of modern when we’re able so long as it’s not distracting. Think 75% classic corporate, 25% modern. Open to black or white design, not sure which might look the best.

Target Market(s)

Senior executives or related government affairs contacts within the agriculture, energy, and defense industries (i.e., potential clients) but located outside of Washington, DC. Most potential clients based in DC with be familiar with both of us and our shared history.

Industry/Entity Type

Consulting

Contact Information for Business Card

Name: Daniel R. Whitlock
Title: Co-Founder & Partner
Address: 418 Bramblewood Ave. SE | Suite 2716 | Washington, D.C. 20019
Phone: (202) 555-0187
Email: Daniel@HollerbyWhitlock.com

Font styles to use
Serif

Colors

Designer to choose only greyscale colors for use in the design.

Requirements
Must have
• Name: Daniel R. Whitlock
Phone: (202) 555-0187

```html
<!DOCTYPE html>
<html lang="en">
<head>
<meta charset="utf-8">
<title>Hollerby Whitlock Group — Business Card</title>
<link href="https://fonts.googleapis.com/css2?family=Jost:wght@300;400;500&display=swap" rel="stylesheet">
<style>
  :root {
    --page-bg: #2b2b2b;
    --card-white: #f4f4f4;
    --card-white-edge: #e2e2e2;
    --card-dark-top: #6a6a6a;
    --card-dark-bottom: #3a3a3a;
    --band-light: #c4c4c4;
    --band-mid: #9a9a9a;
    --band-dark: #6c6c6c;
    --ink-strong: #5a5a5a;
    --ink-soft: #9c9c9c;
    --ink-faint: #b5b5b5;
    --logo-light: #e6e6e6;
  }
  * { margin: 0; padding: 0; box-sizing: border-box; }
  html, body { width: 1200px; height: 900px; overflow: hidden; }
  body {
    background: var(--page-bg);
    font-family: "Jost", sans-serif;
    position: relative;
  }
  .card {
    position: absolute;
    left: 285px;
    width: 630px;
    height: 360px;
    border-radius: 26px;
    overflow: hidden;
    box-shadow: 0 18px 40px rgba(0,0,0,.45);
  }
  /* Front */
  .card-front {
    top: 50px;
    background: linear-gradient(135deg, var(--card-white-edge) 0%, var(--card-white) 45%, #fbfbfb 100%);
  }
  .band-edge {
    position: absolute; left: 0; top: 0; bottom: 0; width: 22px;
    background: var(--band-light);
  }
  .band-main {
    position: absolute; left: 22px; top: 56px; bottom: 0; width: 40px;
    background: var(--band-dark);
  }
  .band-cap {
    position: absolute; left: 22px; top: 0; height: 56px; width: 40px;
    background: var(--band-mid);
  }
  .front-brand {
    position: absolute; left: 90px; top: 36px;
    display: flex; align-items: center; gap: 14px;
  }
  .brand-square {
    width: 34px; height: 34px; background: var(--ink-strong);
  }
  .brand-name {
    font-weight: 400; color: var(--ink-strong);
    line-height: 1;
  }
  .brand-name .brand-main { display: block; font-size: 27px; letter-spacing: 1.5px; }
  .brand-name .brand-sub { display: block; font-size: 12px; letter-spacing: 9px; text-align: right; margin-top: 6px; }
  .holder {
    position: absolute; left: 92px; top: 150px;
  }
  .holder-name {
    font-size: 22px; font-weight: 400; letter-spacing: 1px;
    color: var(--ink-strong); text-transform: uppercase;
  }
  .holder-title {
    font-size: 13px; font-weight: 300; color: var(--ink-soft); margin-top: 2px;
  }
  .contact-list {
    position: absolute; left: 92px; top: 228px;
    list-style: none;
  }
  .contact-item {
    display: flex; align-items: center; gap: 9px;
    font-size: 14px; font-weight: 300; color: var(--ink-soft);
    height: 24px;
  }
  .contact-item svg { width: 16px; height: 16px; flex: none; }
  .contact-item .web-strong { color: var(--ink-strong); font-weight: 400; }
  .address {
    position: absolute; right: 40px; bottom: 34px;
    font-size: 14px; font-weight: 300; color: var(--ink-soft);
    line-height: 1.45; font-style: normal;
  }
  /* Back */
  .card-back {
    top: 490px;
    background: linear-gradient(160deg, var(--card-dark-top) 0%, #4e4e4e 45%, var(--card-dark-bottom) 100%);
    display: flex; align-items: center; justify-content: center;
  }
  .back-brand { display: flex; align-items: center; gap: 20px; }
  .back-brand .brand-square { width: 54px; height: 54px; background: var(--logo-light); }
  .back-brand .brand-name { color: var(--logo-light); }
  .back-brand .brand-main { font-size: 40px; letter-spacing: 2px; }
  .back-brand .brand-sub { font-size: 16px; letter-spacing: 14px; margin-top: 8px; }
</style>
</head>
<body>

<section class="card card-front" aria-label="Business card front">
  <div class="band-edge"></div>
  <div class="band-cap"></div>
  <div class="band-main"></div>

  <div class="front-brand">
    <div class="brand-square"></div>
    <div class="brand-name">
      <span class="brand-main">HOLLERBY WHITLOCK</span>
      <span class="brand-sub">GROUP</span>
    </div>
  </div>

  <div class="holder">
    <div class="holder-name">Daniel R. Whitlock</div>
    <div class="holder-title">Co-Founder &amp; Partner</div>
  </div>

  <ul class="contact-list">
    <li class="contact-item">
      <svg viewBox="0 0 16 16" aria-hidden="true"><circle cx="8" cy="8" r="8" fill="#6a6a6a"/><path d="M5.2 4.3c.4-.3.9-.2 1.1.2l.7 1.2c.2.3.1.7-.2.9l-.5.4c.4.9 1.1 1.6 2 2l.4-.5c.2-.3.6-.4.9-.2l1.2.7c.4.2.5.7.2 1.1-.6.8-1.5 1.1-2.4.7C6.8 10 5.9 9.1 5.1 7.5c-.4-.9-.5-2.4.1-3.2z" fill="#f4f4f4"/></svg>
      (202) 555-0187
    </li>
    <li class="contact-item">
      <svg viewBox="0 0 16 16" aria-hidden="true"><circle cx="8" cy="8" r="8" fill="#6a6a6a"/><rect x="4" y="5.2" width="8" height="5.6" fill="none" stroke="#f4f4f4" stroke-width="1"/><path d="M4 5.4 8 8.4l4-3" fill="none" stroke="#f4f4f4" stroke-width="1"/></svg>
      Daniel@HollerbyWhitlock.com
    </li>
    <li class="contact-item">
      <svg viewBox="0 0 16 16" aria-hidden="true"><circle cx="8" cy="8" r="8" fill="#6a6a6a"/><circle cx="8" cy="8" r="4.2" fill="none" stroke="#f4f4f4" stroke-width="1"/><path d="M3.8 8h8.4M8 3.8c-1.6 1.6-1.6 6.8 0 8.4M8 3.8c1.6 1.6 1.6 6.8 0 8.4" fill="none" stroke="#f4f4f4" stroke-width=".8"/></svg>
      <span>www.<span class="web-strong">HollerbyWhitlock</span>.com</span>
    </li>
  </ul>

  <address class="address">
    418 Bramblewood Ave. SE<br>
    Suite 2716<br>
    Washington, D.C. 20019
  </address>
</section>

<section class="card card-back" aria-label="Business card back">
  <div class="back-brand">
    <div class="brand-square"></div>
    <div class="brand-name">
      <span class="brand-main">HOLLERBY WHITLOCK</span>
      <span class="brand-sub">GROUP</span>
    </div>
  </div>
</section>

</body>
</html>
```